Brisvale app design refresh: 1 new screen, 1 new icon / 11 icons reworked for hi-res, addtnl elements

UPDATE: added task 6

I have a ready design for the app that needs to be updated, but my previous designer can't help due to the workload.

Tasks which need to be accomplished:
1) new Tutorial icon - we used question mark in a
circle for Tutorial request, but I need something different now, because Tutorials are more about assistance than help in a traditional sense; I am thinking about pencil or graduation hat icons, but am open to other ideas
2) guidance on control elements: when you first open Journal screen you should see the bubble around the '+' icon with the text 'Start Here' inside - I need this bubble with text (shape, color etc.)
3) new Tutorial screen - half-transparent dark layer over the screen, where you see the name of the step than some formatted text plus Populate and Continue buttons at the bottom
4) the icons should be reworked for high resolution screens (6 and 6+) - including keyboard, letter A, icons inside the text formatting panel, tag, export, delete (especially keyboard icon)
5) I want one more color introduced for text - now we have only white and black/grey; for example I want the title of the step look different from the text, different color; so, just give me another color which would look great with existing palette
6) Icon for Summary functionality needs to be created; Archive with appropriate themes is attached

Attached is the existing design for Norvex 4s. Your target design should be for 4s and 5/5s and 6/6+

• 4/4s/5/5s/6/6+ quality

```html
<!DOCTYPE html>
<html lang="en">
<head>
<meta charset="utf-8">
<title>Brisvale – Keyboards</title>
<link href="https://fonts.googleapis.com/css2?family=Roboto:wght@300;400;500;700&family=Open+Sans:wght@300;400&family=Playfair+Display:wght@700&display=swap" rel="stylesheet">
<style>
  :root{
    --coral:#fe8f81;
    --teal:#52c8b6;
    --label:#8a8a8a;
    --body-text:#5a5a5a;
    --toolbar:#f4f5f5;
    --kb-bg:#d2d5da;
    --key:#ffffff;
    --key-dark:#b8bdc4;
    --key-text:#222;
    --white:#ffffff;
  }
  *{box-sizing:border-box;margin:0;padding:0}
  html,body{width:1200px;height:1000px;overflow:hidden;background:var(--white)}
  body{position:relative;font-family:"Roboto",sans-serif}

  .banner{position:absolute;left:0;top:33px;width:1200px;height:63px;background:var(--coral);
    color:var(--white);font-weight:500;font-size:42px;text-align:center;line-height:63px}

  .version{position:absolute;top:0;width:360px}
  .version-label{position:absolute;top:128px;width:100%;text-align:center;color:var(--label);font-size:19px;font-weight:300}
  .version-icon{position:absolute;top:182px;left:50%;transform:translateX(-50%)}

  .screen{position:absolute;top:327px;width:353px;height:631px;background:var(--white);overflow:hidden;
    box-shadow:0 0 6px rgba(0,0,0,.18)}
  .status-bar{height:21px;background:var(--teal);color:var(--white);font-size:11.5px;position:relative;
    display:flex;align-items:center;padding:0 8px}
  .status-bar .carrier{font-size:11px;display:flex;align-items:center;gap:4px}
  .status-bar .time{position:absolute;left:0;right:0;text-align:center;font-weight:500;font-size:12.5px}
  .status-bar .battery{margin-left:auto;display:flex;align-items:center;gap:4px;font-size:11px}
  .nav-bar{height:27px;background:var(--teal);color:var(--white);position:relative;text-align:center;
    font-size:15px;font-weight:300;line-height:25px}
  .nav-bar .menu{position:absolute;left:28px;top:7px}
  .nav-bar .help{position:absolute;right:18px;top:4px}

  .journal-text{height:304px;padding:29px 20px 0 22px;font-family:"Open Sans",sans-serif;font-weight:300;
    font-size:10.7px;line-height:13.2px;letter-spacing:.05px;color:var(--body-text)}
  .journal-text p{margin-bottom:13.5px}

  .editor-toolbar{height:39px;background:var(--toolbar);position:relative}
  .editor-toolbar .kb-toggle{position:absolute;left:22px;top:10px}
  .step-dots{position:absolute;left:130px;top:9px;display:flex;gap:2px}
  .step-dot{width:16px;height:16px;border-radius:50%;background:var(--teal);color:var(--white);font-size:8.5px;
    font-weight:500;text-align:center;line-height:13px;border:1.5px solid var(--teal)}
  .step-dot.current{background:var(--coral);border-color:var(--coral)}
  .step-dot.todo{background:var(--white);color:var(--teal)}
  .font-toggle{position:absolute;left:304px;top:8px;font-family:"Playfair Display",serif;color:var(--teal);font-size:17px}

  .keyboard{position:absolute;left:0;top:391px;width:353px;height:240px;background:var(--kb-bg)}
  .format-panel{position:absolute;left:62px;top:388px;width:263px;height:28px;background:var(--teal);z-index:2;
    display:flex;align-items:center;justify-content:space-around;padding:0 8px;color:rgba(255,255,255,.7)}
  .format-panel .glyph{font-size:15px;font-weight:500}
  .format-panel .italic{font-style:italic;font-family:"Playfair Display",serif;font-weight:700}
  .format-panel .underline{text-decoration:underline;font-weight:400}

  .key-row{position:absolute;left:0;width:100%;display:flex;justify-content:space-between}
  .row-1{top:15px;padding:0 3px}
  .row-2{top:74px;padding:0 20px}
  .row-3{top:134px;padding:0 3px}
  .row-4{top:194px;padding:0 3px}
  .key{height:40px;width:31px;background:var(--key);border-radius:5px;box-shadow:0 1px 0 #8e9298;
    font-size:21px;font-weight:300;color:var(--key-text);display:flex;align-items:center;justify-content:center}
  .row-2 .key{width:30px}
  .row-3 .letters{display:flex;gap:5px}
  .key.dark{background:var(--key-dark);width:40px}
  .key.small-label{font-size:15px}
  .row-4 .key{width:36px}
  .row-4 .key.mic{width:28px}
  .row-4 .key.space{width:54px}
  .row-4 .key.return{width:84px}
</style>
</head>
<body>
<header class="banner">Keyboards</header>

<section class="version" style="left:25px">
  <div class="version-label">v1</div>
  <svg class="version-icon" width="142" height="122" viewBox="0 0 142 122">
    <rect x="2" y="2" width="138" height="95" rx="4" fill="none" stroke="var(--teal)" stroke-width="3"/>
    <g fill="var(--teal)">
      <circle cx="24" cy="22" r="4"/><circle cx="39" cy="22" r="4"/><circle cx="54" cy="22" r="4"/><circle cx="69" cy="22" r="4"/><circle cx="84" cy="22" r="4"/><circle cx="99" cy="22" r="4"/><circle cx="114" cy="22" r="4"/>
      <circle cx="31" cy="40" r="4"/><circle cx="46" cy="40" r="4"/><circle cx="61" cy="40" r="4"/><circle cx="76" cy="40" r="4"/><circle cx="91" cy="40" r="4"/><circle cx="106" cy="40" r="4"/>
      <circle cx="39" cy="58" r="4"/><circle cx="54" cy="58" r="4"/><circle cx="69" cy="58" r="4"/><circle cx="84" cy="58" r="4"/><circle cx="99" cy="58" r="4"/>
      <rect x="42" y="74" width="56" height="6" rx="1"/>
    </g>
    <polyline points="54,102 70,117 86,102" fill="none" stroke="var(--teal)" stroke-width="3"/>
  </svg>
  <div class="screen" style="left:5px">
    <div class="status-bar"><span class="carrier">●●●○○ VELA <svg width="13" height="10"><g fill="none" stroke="var(--white)" stroke-width="1.4"><path d="M1 4 A8 8 0 0 1 12 4"/><path d="M3.3 6.3 A5 5 0 0 1 9.7 6.3"/></g><circle cx="6.5" cy="8.6" r="1.2" fill="var(--white)"/></svg></span><span class="time">4:21 PM</span><span class="battery">100% <svg width="26" height="11"><rect x="0.5" y="0.5" width="22" height="10" rx="2" fill="var(--white)" stroke="var(--white)"/><rect x="23" y="3" width="2" height="5" fill="var(--white)"/></svg></span></div>
    <div class="nav-bar"><svg class="menu" width="16" height="12"><g stroke="var(--white)" stroke-width="2"><line x1="0" y1="1" x2="16" y2="1"/><line x1="0" y1="6" x2="16" y2="6"/><line x1="0" y1="11" x2="16" y2="11"/></g></svg>Step A<svg class="help" width="19" height="19"><circle cx="9.5" cy="9.5" r="8" fill="none" stroke="var(--white)" stroke-width="1.5"/><text x="9.5" y="13.5" text-anchor="middle" font-size="11" fill="var(--white)" font-family="Roboto,sans-serif">?</text></svg></div>
    <div class="journal-text">
      <p>These four towns were chosen for the last two weeks of our journey, and each one felt completely unlike the others.</p>
      <p>We began in the northern hills, and after a long ride from the warm, quiet coast we stepped right into a cold, busy mountain town.</p>
      <p>We had spent weeks planning our hiking route, asking friends for advice and tips, reading up on what to pack, etc. and none of us had any idea that we would end up somewhere COLD!</p>
    </div>
    <div class="editor-toolbar">
      <svg class="kb-toggle" width="30" height="24"><rect x="1" y="1" width="28" height="17" rx="1.5" fill="none" stroke="var(--teal)" stroke-width="1.2"/><g fill="var(--teal)"><circle cx="6" cy="5" r="1"/><circle cx="9.5" cy="5" r="1"/><circle cx="13" cy="5" r="1"/><circle cx="16.5" cy="5" r="1"/><circle cx="20" cy="5" r="1"/><circle cx="23.5" cy="5" r="1"/><circle cx="7.5" cy="9" r="1"/><circle cx="11" cy="9" r="1"/><circle cx="14.5" cy="9" r="1"/><circle cx="18" cy="9" r="1"/><circle cx="21.5" cy="9" r="1"/><rect x="10" y="12.5" width="10" height="1.5"/></g><polyline points="11,19.5 15,23 19,19.5" fill="none" stroke="var(--teal)" stroke-width="1.2"/></svg>
      <div class="step-dots"><span class="step-dot">A</span><span class="step-dot">B</span><span class="step-dot current">C</span><span class="step-dot todo">D</span><span class="step-dot todo">E</span></div>
      <span class="font-toggle">A</span>
    </div>
    <div class="format-panel">
      <svg width="22" height="14"><g stroke="currentColor" stroke-width="1.4"><line x1="0" y1="1" x2="22" y2="1"/><line x1="0" y1="5" x2="15" y2="5"/><line x1="0" y1="9" x2="22" y2="9"/><line x1="0" y1="13" x2="15" y2="13"/></g></svg>
      <svg width="22" height="14"><g stroke="currentColor" stroke-width="1.4"><line x1="0" y1="1" x2="22" y2="1"/><line x1="4" y1="5" x2="18" y2="5"/><line x1="0" y1="9" x2="22" y2="9"/><line x1="4" y1="13" x2="18" y2="13"/></g></svg>
      <svg width="22" height="14"><g stroke="currentColor" stroke-width="1.4"><line x1="0" y1="1" x2="22" y2="1"/><line x1="7" y1="5" x2="22" y2="5"/><line x1="0" y1="9" x2="22" y2="9"/><line x1="7" y1="13" x2="22" y2="13"/></g></svg>
      <span class="glyph underline">A</span><span class="glyph italic">I</span><span class="glyph">B</span>
    </div>
    <div class="keyboard">
      <div class="key-row row-1"><span class="key">Q</span><span class="key">W</span><span class="key">E</span><span class="key">R</span><span class="key">T</span><span class="key">Y</span><span class="key">U</span><span class="key">I</span><span class="key">O</span><span class="key">P</span></div>
      <div class="key-row row-2"><span class="key">A</span><span class="key">S</span><span class="key">D</span><span class="key">F</span><span class="key">G</span><span class="key">H</span><span class="key">J</span><span class="key">K</span><span class="key">L</span></div>
      <div class="key-row row-3"><span class="key dark"><svg width="18" height="16"><path d="M9 1 L17 9 H12.5 V15 H5.5 V9 H1 Z" fill="none" stroke="#333" stroke-width="1.2"/></svg></span><span class="letters"><span class="key">Z</span><span class="key">X</span><span class="key">C</span><span class="key">V</span><span class="key">B</span><span class="key">N</span><span class="key">M</span></span><span class="key dark"><svg width="24" height="16"><path d="M7 1 H23 V15 H7 L1 8 Z" fill="none" stroke="#333" stroke-width="1.2"/><path d="M12 5 L18 11 M18 5 L12 11" stroke="#333" stroke-width="1.2"/></svg></span></div>
      <div class="key-row row-4"><span class="key dark small-label">123</span><span class="key dark"><svg width="20" height="20"><g fill="none" stroke="#333" stroke-width="1"><circle cx="10" cy="10" r="8.5"/><ellipse cx="10" cy="10" rx="4" ry="8.5"/><line x1="1.5" y1="10" x2="18.5" y2="10"/><path d="M3 5.5 H17 M3 14.5 H17"/></g></svg></span><span class="key mic"><svg width="12" height="20"><rect x="3" y="1" width="6" height="11" rx="3" fill="none" stroke="#333"/><path d="M1 9 A5 5 0 0 0 11 9 M6 14 V19 M3 19 H9" fill="none" stroke="#333"/></svg></span><span class="key space small-label">space</span><span class="key">@</span><span class="key">.</span><span class="key dark return small-label">return</span></div>
    </div>
  </div>
</section>

<section class="version" style="left:419px">
  <div class="version-label">v2</div>
  <svg class="version-icon" width="142" height="122" viewBox="0 0 142 122">
    <rect x="2" y="6" width="135" height="91" rx="8" fill="none" stroke="var(--teal)" stroke-width="3"/>
    <g fill="var(--teal)">
      <rect x="20" y="22" width="8" height="7" rx="2"/><rect x="36" y="22" width="8" height="7" rx="2"/><rect x="52" y="22" width="8" height="7" rx="2"/><rect x="68" y="22" width="8" height="7" rx="2"/><rect x="84" y="22" width="8" height="7" rx="2"/><rect x="100" y="22" width="8" height="7" rx="2"/><rect x="116" y="22" width="8" height="7" rx="2"/>
      <rect x="28" y="39" width="8" height="7" rx="2"/><rect x="44" y="39" width="8" height="7" rx="2"/><rect x="60" y="39" width="8" height="7" rx="2"/><rect x="76" y="39" width="8" height="7" rx="2"/><rect x="92" y="39" width="8" height="7" rx="2"/><rect x="108" y="39" width="8" height="7" rx="2"/>
      <rect x="36" y="56" width="8" height="7" rx="2"/><rect x="52" y="56" width="8" height="7" rx="2"/><rect x="68" y="56" width="8" height="7" rx="2"/><rect x="84" y="56" width="8" height="7" rx="2"/><rect x="100" y="56" width="8" height="7" rx="2"/>
      <rect x="33" y="74" width="74" height="7" rx="2"/>
    </g>
    <polyline points="57,104 70,116 83,104" fill="none" stroke="var(--teal)" stroke-width="3"/>
  </svg>
  <div class="screen" style="left:5px">
    <div class="status-bar"><span class="carrier">●●●○○ VELA <svg width="13" height="10"><g fill="none" stroke="var(--white)" stroke-width="1.4"><path d="M1 4 A8 8 0 0 1 12 4"/><path d="M3.3 6.3 A5 5 0 0 1 9.7 6.3"/></g><circle cx="6.5" cy="8.6" r="1.2" fill="var(--white)"/></svg></span><span class="time">4:21 PM</span><span class="battery">100% <svg width="26" height="11"><rect x="0.5" y="0.5" width="22" height="10" rx="2" fill="var(--white)" stroke="var(--white)"/><rect x="23" y="3" width="2" height="5" fill="var(--white)"/></svg></span></div>
    <div class="nav-bar"><svg class="menu" width="16" height="12"><g stroke="var(--white)" stroke-width="2"><line x1="0" y1="1" x2="16" y2="1"/><line x1="0" y1="6" x2="16" y2="6"/><line x1="0" y1="11" x2="16" y2="11"/></g></svg>Step A<svg class="help" width="19" height="19"><circle cx="9.5" cy="9.5" r="8" fill="none" stroke="var(--white)" stroke-width="1.5"/><text x="9.5" y="13.5" text-anchor="middle" font-size="11" fill="var(--white)" font-family="Roboto,sans-serif">?</text></svg></div>
    <div class="journal-text">
      <p>These four towns were chosen for the last two weeks of our journey, and each one felt completely unlike the others.</p>
      <p>We began in the northern hills, and after a long ride from the warm, quiet coast we stepped right into a cold, busy mountain town.</p>
      <p>We had spent weeks planning our hiking route, asking friends for advice and tips, reading up on what to pack, etc. and none of us had any idea that we would end up somewhere COLD!</p>
    </div>
    <div class="editor-toolbar">
      <svg class="kb-toggle" width="30" height="24"><rect x="1" y="1" width="28" height="17" rx="2.5" fill="none" stroke="var(--teal)" stroke-width="1.2"/><g fill="var(--teal)"><rect x="5" y="4" width="2" height="2"/><rect x="8.5" y="4" width="2" height="2"/><rect x="12" y="4" width="2" height="2"/><rect x="15.5" y="4" width="2" height="2"/><rect x="19" y="4" width="2" height="2"/><rect x="22.5" y="4" width="2" height="2"/><rect x="7" y="8" width="2" height="2"/><rect x="10.5" y="8" width="2" height="2"/><rect x="14" y="8" width="2" height="2"/><rect x="17.5" y="8" width="2" height="2"/><rect x="21" y="8" width="2" height="2"/><rect x="10" y="12.5" width="10" height="1.5"/></g><polyline points="11,19.5 15,23 19,19.5" fill="none" stroke="var(--teal)" stroke-width="1.2"/></svg>
      <div class="step-dots"><span class="step-dot">A</span><span class="step-dot">B</span><span class="step-dot current">C</span><span class="step-dot todo">D</span><span class="step-dot todo">E</span></div>
      <span class="font-toggle">A</span>
    </div>
    <div class="format-panel">
      <svg width="22" height="14"><g stroke="currentColor" stroke-width="1.4"><line x1="0" y1="1" x2="22" y2="1"/><line x1="0" y1="5" x2="15" y2="5"/><line x1="0" y1="9" x2="22" y2="9"/><line x1="0" y1="13" x2="15" y2="13"/></g></svg>
      <svg width="22" height="14"><g stroke="currentColor" stroke-width="1.4"><line x1="0" y1="1" x2="22" y2="1"/><line x1="4" y1="5" x2="18" y2="5"/><line x1="0" y1="9" x2="22" y2="9"/><line x1="4" y1="13" x2="18" y2="13"/></g></svg>
      <svg width="22" height="14"><g stroke="currentColor" stroke-width="1.4"><line x1="0" y1="1" x2="22" y2="1"/><line x1="7" y1="5" x2="22" y2="5"/><line x1="0" y1="9" x2="22" y2="9"/><line x1="7" y1="13" x2="22" y2="13"/></g></svg>
      <span class="glyph underline">A</span><span class="glyph italic">I</span><span class="glyph">B</span>
    </div>
    <div class="keyboard">
      <div class="key-row row-1"><span class="key">Q</span><span class="key">W</span><span class="key">E</span><span class="key">R</span><span class="key">T</span><span class="key">Y</span><span class="key">U</span><span class="key">I</span><span class="key">O</span><span class="key">P</span></div>
      <div class="key-row row-2"><span class="key">A</span><span class="key">S</span><span class="key">D</span><span class="key">F</span><span class="key">G</span><span class="key">H</span><span class="key">J</span><span class="key">K</span><span class="key">L</span></div>
      <div class="key-row row-3"><span class="key dark"><svg width="18" height="16"><path d="M9 1 L17 9 H12.5 V15 H5.5 V9 H1 Z" fill="none" stroke="#333" stroke-width="1.2"/></svg></span><span class="letters"><span class="key">Z</span><span class="key">X</span><span class="key">C</span><span class="key">V</span><span class="key">B</span><span class="key">N</span><span class="key">M</span></span><span class="key dark"><svg width="24" height="16"><path d="M7 1 H23 V15 H7 L1 8 Z" fill="none" stroke="#333" stroke-width="1.2"/><path d="M12 5 L18 11 M18 5 L12 11" stroke="#333" stroke-width="1.2"/></svg></span></div>
      <div class="key-row row-4"><span class="key dark small-label">123</span><span class="key dark"><svg width="20" height="20"><g fill="none" stroke="#333" stroke-width="1"><circle cx="10" cy="10" r="8.5"/><ellipse cx="10" cy="10" rx="4" ry="8.5"/><line x1="1.5" y1="10" x2="18.5" y2="10"/><path d="M3 5.5 H17 M3 14.5 H17"/></g></svg></span><span class="key mic"><svg width="12" height="20"><rect x="3" y="1" width="6" height="11" rx="3" fill="none" stroke="#333"/><path d="M1 9 A5 5 0 0 0 11 9 M6 14 V19 M3 19 H9" fill="none" stroke="#333"/></svg></span><span class="key space small-label">space</span><span class="key">@</span><span class="key">.</span><span class="key dark return small-label">return</span></div>
    </div>
  </div>
</section>

<section class="version" style="left:815px">
  <div class="version-label">v3</div>
  <svg class="version-icon" width="142" height="122" viewBox="0 0 142 122">
    <rect x="10" y="6" width="124" height="84" rx="4" fill="none" stroke="var(--teal)" stroke-width="2.5"/>
    <g fill="var(--teal)">
      <rect x="25" y="15" width="8" height="8"/><rect x="40" y="15" width="8" height="8"/><rect x="55" y="15" width="8" height="8"/><rect x="70" y="15" width="8" height="8"/><rect x="85" y="15" width="8" height="8"/><rect x="100" y="15" width="8" height="8"/><rect x="115" y="15" width="8" height="8"/>
      <rect x="24" y="34" width="8" height="8"/><rect x="40" y="34" width="8" height="8"/><rect x="56" y="34" width="8" height="8"/><rect x="72" y="34" width="8" height="8"/><rect x="88" y="34" width="8" height="8"/><rect x="104" y="34" width="8" height="8"/><rect x="118" y="34" width="8" height="8"/>
      <rect x="32" y="53" width="8" height="8"/><rect x="48" y="53" width="8" height="8"/><rect x="64" y="53" width="8" height="8"/><rect x="80" y="53" width="8" height="8"/><rect x="96" y="53" width="8" height="8"/>
      <rect x="35" y="70" width="72" height="7"/>
    </g>
    <polyline points="59,98 72,110 85,98" fill="none" stroke="var(--teal)" stroke-width="2.5"/>
  </svg>
  <div class="screen" style="left:5px">
    <div class="status-bar"><span class="carrier">●●●○○ VELA <svg width="13" height="10"><g fill="none" stroke="var(--white)" stroke-width="1.4"><path d="M1 4 A8 8 0 0 1 12 4"/><path d="M3.3 6.3 A5 5 0 0 1 9.7 6.3"/></g><circle cx="6.5" cy="8.6" r="1.2" fill="var(--white)"/></svg></span><span class="time">4:21 PM</span><span class="battery">100% <svg width="26" height="11"><rect x="0.5" y="0.5" width="22" height="10" rx="2" fill="var(--white)" stroke="var(--white)"/><rect x="23" y="3" width="2" height="5" fill="var(--white)"/></svg></span></div>
    <div class="nav-bar"><svg class="menu" width="16" height="12"><g stroke="var(--white)" stroke-width="2"><line x1="0" y1="1" x2="16" y2="1"/><line x1="0" y1="6" x2="16" y2="6"/><line x1="0" y1="11" x2="16" y2="11"/></g></svg>Step A<svg class="help" width="19" height="19"><circle cx="9.5" cy="9.5" r="8" fill="none" stroke="var(--white)" stroke-width="1.5"/><text x="9.5" y="13.5" text-anchor="middle" font-size="11" fill="var(--white)" font-family="Roboto,sans-serif">?</text></svg></div>
    <div class="journal-text">
      <p>These four towns were chosen for the last two weeks of our journey, and each one felt completely unlike the others.</p>
      <p>We began in the northern hills, and after a long ride from the warm, quiet coast we stepped right into a cold, busy mountain town.</p>
      <p>We had spent weeks planning our hiking route, asking friends for advice and tips, reading up on what to pack, etc. and none of us had any idea that we would end up somewhere COLD!</p>
    </div>
    <div class="editor-toolbar">
      <svg class="kb-toggle" width="30" height="24"><rect x="1" y="1" width="28" height="17" rx="1" fill="none" stroke="var(--teal)" stroke-width="1.2"/><g fill="var(--teal)"><rect x="5" y="4" width="2" height="2"/><rect x="8.5" y="4" width="2" height="2"/><rect x="12" y="4" width="2" height="2"/><rect x="15.5" y="4" width="2" height="2"/><rect x="19" y="4" width="2" height="2"/><rect x="22.5" y="4" width="2" height="2"/><rect x="7" y="8" width="2" height="2"/><rect x="10.5" y="8" width="2" height="2"/><rect x="14" y="8" width="2" height="2"/><rect x="17.5" y="8" width="2" height="2"/><rect x="21" y="8" width="2" height="2"/><rect x="10" y="12.5" width="10" height="1.5"/></g><polyline points="11,19.5 15,23 19,19.5" fill="none" stroke="var(--teal)" stroke-width="1.2"/></svg>
      <div class="step-dots"><span class="step-dot">A</span><span class="step-dot">B</span><span class="step-dot current">C</span><span class="step-dot todo">D</span><span class="step-dot todo">E</span></div>
      <span class="font-toggle">A</span>
    </div>
    <div class="format-panel">
      <svg width="22" height="14"><g stroke="currentColor" stroke-width="1.4"><line x1="0" y1="1" x2="22" y2="1"/><line x1="0" y1="5" x2="15" y2="5"/><line x1="0" y1="9" x2="22" y2="9"/><line x1="0" y1="13" x2="15" y2="13"/></g></svg>
      <svg width="22" height="14"><g stroke="currentColor" stroke-width="1.4"><line x1="0" y1="1" x2="22" y2="1"/><line x1="4" y1="5" x2="18" y2="5"/><line x1="0" y1="9" x2="22" y2="9"/><line x1="4" y1="13" x2="18" y2="13"/></g></svg>
      <svg width="22" height="14"><g stroke="currentColor" stroke-width="1.4"><line x1="0" y1="1" x2="22" y2="1"/><line x1="7" y1="5" x2="22" y2="5"/><line x1="0" y1="9" x2="22" y2="9"/><line x1="7" y1="13" x2="22" y2="13"/></g></svg>
      <span class="glyph underline">A</span><span class="glyph italic">I</span><span class="glyph">B</span>
    </div>
    <div class="keyboard">
      <div class="key-row row-1"><span class="key">Q</span><span class="key">W</span><span class="key">E</span><span class="key">R</span><span class="key">T</span><span class="key">Y</span><span class="key">U</span><span class="key">I</span><span class="key">O</span><span class="key">P</span></div>
      <div class="key-row row-2"><span class="key">A</span><span class="key">S</span><span class="key">D</span><span class="key">F</span><span class="key">G</span><span class="key">H</span><span class="key">J</span><span class="key">K</span><span class="key">L</span></div>
      <div class="key-row row-3"><span class="key dark"><svg width="18" height="16"><path d="M9 1 L17 9 H12.5 V15 H5.5 V9 H1 Z" fill="none" stroke="#333" stroke-width="1.2"/></svg></span><span class="letters"><span class="key">Z</span><span class="key">X</span><span class="key">C</span><span class="key">V</span><span class="key">B</span><span class="key">N</span><span class="key">M</span></span><span class="key dark"><svg width="24" height="16"><path d="M7 1 H23 V15 H7 L1 8 Z" fill="none" stroke="#333" stroke-width="1.2"/><path d="M12 5 L18 11 M18 5 L12 11" stroke="#333" stroke-width="1.2"/></svg></span></div>
      <div class="key-row row-4"><span class="key dark small-label">123</span><span class="key dark"><svg width="20" height="20"><g fill="none" stroke="#333" stroke-width="1"><circle cx="10" cy="10" r="8.5"/><ellipse cx="10" cy="10" rx="4" ry="8.5"/><line x1="1.5" y1="10" x2="18.5" y2="10"/><path d="M3 5.5 H17 M3 14.5 H17"/></g></svg></span><span class="key mic"><svg width="12" height="20"><rect x="3" y="1" width="6" height="11" rx="3" fill="none" stroke="#333"/><path d="M1 9 A5 5 0 0 0 11 9 M6 14 V19 M3 19 H9" fill="none" stroke="#333"/></svg></span><span class="key space small-label">space</span><span class="key">@</span><span class="key">.</span><span class="key dark return small-label">return</span></div>
    </div>
  </div>
</section>
</body>
</html>
```